Annual Event PPT Template

We need a PowerPoint template to use for a big annual event we host. Attached is the logo we use for everything. You can also reference our website (listed below) and our letterhead for design inspiration.

Please be sure to include our contact information on all of the PPT slides:
1. Phone: 802-417-3926
2. Address: 342 Fernwick Hollow Road, Corwin Falls, NH 03782
3. Website: www.QuarvelSys.com

```html
<!DOCTYPE html>
<html lang="en">
<head>
<meta charset="utf-8">
<title>QuarvelSys Annual Event Slide</title>
<link href="https://fonts.googleapis.com/css2?family=Montserrat:wght@400;700&display=swap" rel="stylesheet">
<style>
  :root {
    --brand-navy: #235a84;
    --dot-blue: #6795bf;
    --dot-orange: #e57521;
    --edge-grey: #d2d3d5;
    --mid-grey: #ebecec;
    --center-white: #ffffff;
    --footer-blue: #6a95bf;
  }
  html, body {
    margin: 0;
    padding: 0;
    width: 1200px;
    height: 675px;
    overflow: hidden;
  }
  .slide {
    position: relative;
    width: 1200px;
    height: 675px;
    overflow: hidden;
    background: linear-gradient(90deg,
      var(--edge-grey) 0%,
      var(--mid-grey) 22%,
      var(--center-white) 56%,
      var(--mid-grey) 82%,
      var(--edge-grey) 100%);
    font-family: "Montserrat", sans-serif;
  }
  .brand-name {
    position: absolute;
    left: 71px;
    top: 30px;
    margin: 0;
    font-family: "Montserrat", sans-serif;
    font-weight: 700;
    font-size: 44px;
    line-height: 1;
    letter-spacing: -0.5px;
    color: var(--brand-navy);
  }
  .dots {
    position: absolute;
    inset: 0;
    width: 1200px;
    height: 675px;
  }
  .dot-blue { fill: var(--dot-blue); }
  .dot-orange { fill: var(--dot-orange); }
  .contact-line {
    position: absolute;
    left: 0;
    right: 0;
    top: 639px;
    margin: 0;
    padding-left: 56px;
    text-align: center;
    font-family: "Montserrat", sans-serif;
    font-weight: 400;
    font-size: 17.5px;
    line-height: 22px;
    letter-spacing: 0.3px;
    color: var(--footer-blue);
    white-space: nowrap;
  }
</style>
</head>
<body>
  <main class="slide">
    <h1 class="brand-name">QuarvelSys</h1>

    <svg class="dots" viewBox="0 0 1200 675" aria-hidden="true">
      <g class="dots-top-right">
        <circle class="dot-blue" cx="1184" cy="58" r="40"/>
        <circle class="dot-orange" cx="1108" cy="140" r="22"/>
        <circle class="dot-blue" cx="1046" cy="86" r="12"/>
        <circle class="dot-blue" cx="1150" cy="214" r="30"/>
        <circle class="dot-orange" cx="1062" cy="232" r="7"/>
      </g>
      <g class="dots-bottom-left">
        <circle class="dot-orange" cx="70" cy="512" r="13"/>
        <circle class="dot-blue" cx="146" cy="548" r="8"/>
        <circle class="dot-blue" cx="30" cy="590" r="22"/>
        <circle class="dot-blue" cx="112" cy="628" r="14"/>
        <circle class="dot-orange" cx="16" cy="672" r="30"/>
      </g>
    </svg>

    <p class="contact-line">802-417-3926 | 342 Fernwick Hollow Road, Corwin Falls, NH 03782 | www.QuarvelSys.com</p>
  </main>
</body>
</html>
```